Business card, postcard, pocket folder

We are a real estate team and have had a new logo designed. From this, we need the following deliverables:- Business Cards (double-sided)- Just Listed / Just Sold Postcards (double-sided)- Pocket Folder. See logo attached.More work possible for the winning designer.
There are 5 members of the team, so head shots should be easily changed and possible for a group photo might be a good idea for the pocket folder but not 100% neccessary.
Target Market(s)
Real estate
Industry/Entity Type
Real Estate
Font styles to use
Serif
Sans Serif
Requirements
Must have
- Business cards and postcards must have a head shot on them.

```html
<!DOCTYPE html>
<html lang="en">
<head>
<meta charset="utf-8">
<title>Harwell Group – Just Listed / Just Sold Postcard</title>
<link href="https://fonts.googleapis.com/css2?family=Montserrat:wght@600;700&family=Open+Sans:wght@400;600&family=Merriweather:wght@400&display=swap" rel="stylesheet">
<style>
  :root {
    --backdrop: #c4c4c4;
    --paper: #ffffff;
    --brand-blue: #23409a;
    --brand-red: #e31b23;
    --ink: #222222;
    --sky-top: #4f86cf;
    --sky-bottom: #bcd4ec;
    --lawn: #8a9a58;
    --house: #c9ab84;
  }
  * { box-sizing: border-box; margin: 0; padding: 0; }
  html, body { width: 1200px; height: 1200px; overflow: hidden; }
  body {
    background: var(--backdrop);
    font-family: "Open Sans", sans-serif;
    color: var(--ink);
    position: relative;
  }
  .postcard {
    position: absolute;
    left: 100px;
    width: 1000px;
    height: 500px;
    background: var(--paper);
    box-shadow: 0 6px 18px rgba(0,0,0,.25);
  }
  .postcard--front { top: 60px; }
  .postcard--back { top: 640px; }

  /* Front */
  .hero {
    position: absolute;
    left: 24px; right: 24px; top: 22px;
    height: 300px;
    background: linear-gradient(180deg, var(--sky-top) 0%, var(--sky-bottom) 55%, var(--house) 75%, var(--lawn) 100%);
  }
  .brand-name {
    position: absolute;
    left: 26px; top: 72px;
    font-family: "Montserrat", sans-serif;
    font-weight: 700;
    font-size: 26px;
    color: var(--brand-blue);
    display: flex; align-items: center; gap: 8px;
  }
  .brand-name::before {
    content: "";
    width: 14px; height: 14px;
    background: var(--brand-red);
  }
  .callout-band {
    position: absolute;
    left: 0; right: 0; bottom: 0;
    height: 50px;
    background: var(--brand-blue);
    color: #fff;
    display: flex; align-items: center;
    padding-left: 26px;
    gap: 14px;
    font-family: "Montserrat", sans-serif;
    font-weight: 600;
    font-size: 16.5px;
  }
  .callout-band .callout-phone {
    font-family: "Merriweather", serif;
    font-size: 22px;
  }
  .contact-list {
    position: absolute;
    left: 48px; top: 380px;
    display: flex; gap: 16px;
  }
  .icon-rail {
    width: 26px; height: 108px;
    background: var(--brand-red);
    border-radius: 13px;
    display: flex; flex-direction: column;
    justify-content: space-around; align-items: center;
    padding: 6px 0;
  }
  .icon-rail svg { width: 14px; height: 14px; }
  .contact-lines {
    font-family: "Merriweather", serif;
    font-size: 15px;
    line-height: 27px;
    margin-top: -4px;
  }
  .team-photo {
    position: absolute;
    right: 40px; top: 345px;
    width: 250px; height: 145px;
    background: linear-gradient(180deg, #f2f2f2 0%, #8a8580 40%, #4a4848 100%);
    border-radius: 40px 40px 0 0;
  }

  /* Back */
  .listing-grid {
    position: absolute;
    left: 70px; right: 50px; top: 50px;
    display: grid;
    grid-template-columns: repeat(3, 1fr);
    column-gap: 30px;
    row-gap: 40px;
  }
  .listing { position: relative; }
  .listing-photo {
    height: 112px;
    background: linear-gradient(180deg, var(--sky-top) 0%, var(--sky-bottom) 45%, var(--house) 70%, var(--lawn) 100%);
  }
  .status-ribbon {
    position: absolute;
    left: -28px; top: 8px;
    width: 140px; height: 34px;
    background: var(--brand-red);
    color: #fff;
    font-size: 15px;
    border-radius: 4px;
    transform: rotate(-33deg);
    display: flex; align-items: center; justify-content: center;
  }
  .listing-title {
    font-family: "Montserrat", sans-serif;
    font-weight: 600;
    font-size: 15px;
    color: var(--brand-red);
    margin-top: 14px;
  }
  .listing-text {
    font-size: 10px;
    line-height: 13px;
    margin-top: 2px;
  }
  .listing-specs {
    display: flex; align-items: center; gap: 10px;
    font-size: 11.5px;
    margin-top: 8px;
  }
  .listing-specs svg { height: 12px; }
</style>
</head>
<body>

<section class="postcard postcard--front">
  <div class="hero" role="img" aria-label="Photograph of a large two-storey brick and stucco family home under a blue sky">
    <div class="brand-name">Harwell Group</div>
    <div class="callout-band">
      <span>THINKING OF SELLING OR NEED SOME ADVICE? CALL US TODAY!</span>
      <span class="callout-phone">111-222-3456</span>
    </div>
  </div>

  <div class="contact-list">
    <div class="icon-rail">
      <svg viewBox="0 0 14 14"><path d="M7 1a4 4 0 0 0-4 4c0 3 4 8 4 8s4-5 4-8a4 4 0 0 0-4-4zm0 5.5A1.5 1.5 0 1 1 7 3.5a1.5 1.5 0 0 1 0 3z" fill="#fff"/></svg>
      <svg viewBox="0 0 14 14"><path d="M2 4c0-1 1-2 2-2h6c1 0 2 1 2 2v1H9V4H5v1H2zM3 6h8l1 6H2z" fill="#fff"/></svg>
      <svg viewBox="0 0 14 14"><rect x="1" y="3" width="12" height="8" fill="#fff"/><path d="M1 3l6 5 6-5" stroke="#e31b23" fill="none"/></svg>
      <svg viewBox="0 0 14 14"><circle cx="7" cy="7" r="5.5" fill="none" stroke="#fff"/><ellipse cx="7" cy="7" rx="2.3" ry="5.5" fill="none" stroke="#fff"/><path d="M1.5 7h11" stroke="#fff"/></svg>
    </div>
    <div class="contact-lines">
      <p>Suite 102 , Street 20, Zip code 1122 City, Country</p>
      <p>111-222-3456</p>
      <p>info@harwellgroup.com</p>
      <p>www.harwellgroup.com</p>
    </div>
  </div>

  <div class="team-photo" role="img" aria-label="Group head shot of the real estate team in business suits"></div>
</section>

<section class="postcard postcard--back">
  <div class="listing-grid">
    <article class="listing">
      <div class="listing-photo" role="img" aria-label="Photograph of a brick family home with lawn"></div>
      <div class="status-ribbon">Sold</div>
      <h3 class="listing-title">123 Voltair Street in Sans</h3>
      <p class="listing-text">Lorem ipsum dolor sit amet, graecequidam-eoste, facetediceretvituperatoribusest at.</p>
      <div class="listing-specs">
        <svg viewBox="0 0 24 12" width="24"><path d="M1 1v10M1 8h22v3M1 6h6V3h16v5" stroke="#23409a" stroke-width="2" fill="none"/></svg><span>6 Beds</span>
        <svg viewBox="0 0 12 12" width="12"><path d="M2 12V2h5v3M4 7h7v2H4z" stroke="#23409a" stroke-width="1.6" fill="none"/></svg><span>6 Baths</span>
      </div>
    </article>
    <article class="listing">
      <div class="listing-photo" role="img" aria-label="Photograph of a grey craftsman house with trees"></div>
      <div class="status-ribbon">Sold</div>
      <h3 class="listing-title">123 Voltair Street in Sans</h3>
      <p class="listing-text">Lorem ipsum dolor sit amet, graecequidam-eoste, facetediceretvituperatoribusest at.</p>
      <div class="listing-specs">
        <svg viewBox="0 0 24 12" width="24"><path d="M1 1v10M1 8h22v3M1 6h6V3h16v5" stroke="#23409a" stroke-width="2" fill="none"/></svg><span>6 Beds</span>
        <svg viewBox="0 0 12 12" width="12"><path d="M2 12V2h5v3M4 7h7v2H4z" stroke="#23409a" stroke-width="1.6" fill="none"/></svg><span>6 Baths</span>
      </div>
    </article>
    <article class="listing">
      <div class="listing-photo" role="img" aria-label="Photograph of a stucco home with brick chimney"></div>
      <div class="status-ribbon">Sold</div>
      <h3 class="listing-title">123 Voltair Street in Sans</h3>
      <p class="listing-text">Lorem ipsum dolor sit amet, graecequidam-eoste, facetediceretvituperatoribusest at.</p>
      <div class="listing-specs">
        <svg viewBox="0 0 24 12" width="24"><path d="M1 1v10M1 8h22v3M1 6h6V3h16v5" stroke="#23409a" stroke-width="2" fill="none"/></svg><span>6 Beds</span>
        <svg viewBox="0 0 12 12" width="12"><path d="M2 12V2h5v3M4 7h7v2H4z" stroke="#23409a" stroke-width="1.6" fill="none"/></svg><span>6 Baths</span>
      </div>
    </article>
    <article class="listing">
      <div class="listing-photo" role="img" aria-label="Photograph of a brick family home with lawn"></div>
      <div class="status-ribbon">Listed</div>
      <h3 class="listing-title">123 Voltair Street in Sans</h3>
      <p class="listing-text">Lorem ipsum dolor sit amet, graecequidam-eoste, facetediceretvituperatoribusest at.</p>
      <div class="listing-specs">
        <svg viewBox="0 0 24 12" width="24"><path d="M1 1v10M1 8h22v3M1 6h6V3h16v5" stroke="#23409a" stroke-width="2" fill="none"/></svg><span>6 Beds</span>
        <svg viewBox="0 0 12 12" width="12"><path d="M2 12V2h5v3M4 7h7v2H4z" stroke="#23409a" stroke-width="1.6" fill="none"/></svg><span>6 Baths</span>
      </div>
    </article>
    <article class="listing">
      <div class="listing-photo" role="img" aria-label="Photograph of a grey craftsman house with trees"></div>
      <div class="status-ribbon">Listed</div>
      <h3 class="listing-title">123 Voltair Street in Sans</h3>
      <p class="listing-text">Lorem ipsum dolor sit amet, graecequidam-eoste, facetediceretvituperatoribusest at.</p>
      <div class="listing-specs">
        <svg viewBox="0 0 24 12" width="24"><path d="M1 1v10M1 8h22v3M1 6h6V3h16v5" stroke="#23409a" stroke-width="2" fill="none"/></svg><span>6 Beds</span>
        <svg viewBox="0 0 12 12" width="12"><path d="M2 12V2h5v3M4 7h7v2H4z" stroke="#23409a" stroke-width="1.6" fill="none"/></svg><span>6 Baths</span>
      </div>
    </article>
    <article class="listing">
      <div class="listing-photo" role="img" aria-label="Photograph of a stucco home with brick chimney"></div>
      <div class="status-ribbon">Listed</div>
      <h3 class="listing-title">123 Voltair Street in Sans</h3>
      <p class="listing-text">Lorem ipsum dolor sit amet, graecequidam-eoste, facetediceretvituperatoribusest at.</p>
      <div class="listing-specs">
        <svg viewBox="0 0 24 12" width="24"><path d="M1 1v10M1 8h22v3M1 6h6V3h16v5" stroke="#23409a" stroke-width="2" fill="none"/></svg><span>6 Beds</span>
        <svg viewBox="0 0 12 12" width="12"><path d="M2 12V2h5v3M4 7h7v2H4z" stroke="#23409a" stroke-width="1.6" fill="none"/></svg><span>6 Baths</span>
      </div>
    </article>
  </div>
</section>

</body>
</html>
```